RW SURFACING CONTRACTORS LTD PRESENTATION FOLDER

I need a Presentation Folder please to contain information about our services.

We are a Flooring Contractor - for information about our business please view our website: www.rwsurfacing.co.nz

Please refer to our new brochure attached - it must fit this style and suit our brand.
Look forward to your ideas.

Also our logo needs a couple of quick changes -
Refer attached - can you please change a line and add a line -

logo
Concrete Grinding and Polishing
Resin Floors and Floor Toppings
Concrete Prep and Non Slip Coatings

Thanks Tess
Updates

Hi ALL - I just need a simple PRESENTATION FOLDER.

I already have a brochure so I don't need the same information again on my Presentation Folder.
Just something simple - with just our logo really - for ideas look at Presentation folders at Orbel Press.
I just like the colours and style of the brochure and thought these could help you.
The presentation folder will house that brochure and other bits of information.
I hope this helps
TessĀ 

I just added our revised logo - and gave more specific details about what we are after - refer notes.

Thanks, TessĀ 

Industry/Entity Type

Business

Requirements
Must have
• I just added our updated LOGO - thought this would help match the blue.

I would like LOGO on front page with key words Quality, Value, Experience.
Plain blue inside
Back please add our guarantee, and contact details including website and email etc.

This one will come down to lay out which must match our brochure which was provided. Thank you.

```html
<!DOCTYPE html>
<html lang="en">
<head>
<meta charset="utf-8">
<title>RW Surfacing Contractors – Presentation Folder</title>
<link href="https://fonts.googleapis.com/css2?family=Arimo:wght@400;700&display=swap" rel="stylesheet">
<style>
  :root {
    --folder-blue: #7487c0;
    --die-line: #a9b8de;
    --white: #ffffff;
    --brand-red: #d9262b;
    --text-red: #b3242a;
    --brand-slate: #6f7fb4;
    --ink: #1c1c1c;
    --photo-sky: #c9d3dc;
    --photo-house: #e9ecee;
    --photo-pool: #4a86c0;
  }
  * { margin: 0; padding: 0; box-sizing: border-box; }
  html, body { width: 836px; height: 1200px; overflow: hidden; }
  body { background: var(--folder-blue); font-family: "Arimo", Arial, sans-serif; }
  .folder { position: relative; width: 836px; height: 1200px; background: var(--folder-blue); }
  .dielines { position: absolute; inset: 0; }

  /* Back cover */
  .back-cover { position: absolute; left: 84px; top: 0; width: 373px; height: 507px; }
  .guarantee {
    position: absolute; top: 38px; left: 0; width: 100%;
    color: var(--white); text-align: center; font-size: 15.5px; line-height: 24px;
  }
  .quote-band {
    position: absolute; top: 213px; left: 0; width: 100%; height: 62px;
    background: var(--white); color: var(--text-red);
    text-align: center; font-size: 10.5px; line-height: 14px; padding-top: 8px;
  }
  .lower-band { position: absolute; top: 344px; left: 0; width: 100%; height: 163px; background: var(--white); }
  .star { position: absolute; left: 134px; top: 272px; width: 96px; height: 92px; }
  .wordmark { display: flex; align-items: center; gap: 5px; }
  .wordmark-square { width: 10px; height: 10px; background: var(--brand-slate); flex: none; }
  .wordmark-name { font-weight: 700; color: var(--brand-slate); letter-spacing: .3px; }
  .back-logo { position: absolute; top: 380px; left: 0; width: 100%; display: flex; flex-direction: column; align-items: center; }
  .back-logo .wordmark-name { font-size: 8.5px; }
  .services-small { font-size: 5px; line-height: 6px; text-align: center; color: var(--ink); margin-top: 2px; }
  .contact { position: absolute; left: 92px; top: 434px; font-size: 8.6px; line-height: 12px; color: var(--ink); }
  .contact p + p { margin-top: 4px; }
  .contact .social { display: flex; align-items: center; gap: 8px; margin-top: 6px; }
  .social-square { width: 12px; height: 12px; background: var(--brand-slate); }

  /* Front cover */
  .front-cover { position: absolute; left: 463px; top: 0; width: 373px; height: 507px; background: var(--white); overflow: hidden; }
  .cover-photo {
    position: absolute; left: 0; top: 0; width: 373px; height: 330px;
    background: linear-gradient(180deg, var(--photo-sky) 0%, var(--photo-house) 45%, var(--photo-pool) 100%);
  }
  .swoosh { position: absolute; left: 0; top: 280px; width: 373px; height: 70px; }
  .front-logo {
    position: absolute; left: 128px; top: 322px; width: 140px; height: 74px;
    display: flex; flex-direction: column; align-items: center; justify-content: center;
  }
  .front-logo .wordmark-name { font-size: 11px; }
  .front-logo .services-small { font-size: 6px; line-height: 7.5px; margin-top: 4px; font-weight: 700; }
  .keywords { position: absolute; left: 53px; top: 416px; font-weight: 700; font-size: 24px; line-height: 40px; color: var(--brand-slate); }
  .keywords .second { padding-left: 58px; }
  .keywords .quality { color: var(--brand-red); }

  /* Side tab */
  .glue-flap { position: absolute; left: 0; top: 213px; width: 84px; height: 294px; background: var(--white); }
</style>
</head>
<body>
<main class="folder">

  <div class="glue-flap"></div>

  <section class="back-cover">
    <p class="guarantee">Our guarantee to you<br>Have complete<br>peace of mind<br>when dealing with us,<br>as we provide a<br>workmanship guarantee<br>on all services.</p>
    <p class="quote-band">Arrange your free quote and consultation<br>for concrete polishing, concrete preparation,<br>non-slip coatings or resin floor toppings...</p>
    <div class="lower-band"></div>
    <svg class="star" viewBox="0 0 100 95" aria-hidden="true">
      <polygon points="50,0 62,35 100,36 70,58 81,95 50,73 19,95 30,58 0,36 38,35" fill="#e3232a"/>
    </svg>
    <div class="back-logo">
      <div class="wordmark"><span class="wordmark-square"></span><span class="wordmark-name">RW SURFACING CONTRACTORS</span></div>
      <p class="services-small">Concrete Grinding and Polishing<br>Resin Floors and Floor Toppings<br>Concrete Prep and Non Slip Coatings</p>
    </div>
    <div class="contact">
      <p>Freephone: 0800 555 014 &nbsp;&nbsp;&nbsp; Fax: 09 555 0172</p>
      <p>Postal address: PO Box 412, Auckland, NZ 0600<br>Email: info@rwsurfacing.co.nz &nbsp; Web: www.rwsurfacing.co.nz</p>
      <p class="social"><span class="social-square"></span>www.rwsurfacing.co.nz/news</p>
    </div>
  </section>

  <section class="front-cover">
    <div class="cover-photo" role="img" aria-label="Photo of a modern white house with a pool and patio, with round inset photos of polished and coated floors"></div>
    <svg class="swoosh" viewBox="0 0 373 70" preserveAspectRatio="none" aria-hidden="true">
      <path d="M0,70 L0,44 C120,4 260,0 373,22 L373,70 Z" fill="#d9262b"/>
      <path d="M0,70 L0,52 C120,14 260,10 373,32 L373,70 Z" fill="#5a74b8"/>
      <path d="M0,70 L0,60 C120,24 260,20 373,42 L373,70 Z" fill="#ffffff"/>
    </svg>
    <div class="front-logo">
      <div class="wordmark"><span class="wordmark-square"></span><span class="wordmark-name">RW SURFACING CONTRACTORS</span></div>
      <p class="services-small">Concrete Grinding and Polishing<br>Resin Floors and Floor Toppings<br>Concrete Prep and Non Slip Coatings</p>
    </div>
    <p class="keywords"><span>Experience,</span><br><span class="second"><span class="quality">Quality,</span> Value</span></p>
  </section>

  <svg class="dielines" viewBox="0 0 836 1200" aria-hidden="true" fill="none" stroke="var(--die-line)" stroke-width="1">
    <line x1="84" y1="0" x2="84" y2="507"/>
    <line x1="460" y1="0" x2="460" y2="507"/>
    <line x1="0" y1="520" x2="836" y2="520"/>
    <path d="M84,90 L10,120 L10,520"/>
    <circle cx="38" cy="248" r="8"/>
    <circle cx="38" cy="398" r="8"/>
    <path d="M40,475 L60,500"/>
    <path d="M84,520 L100,560 L440,560 L457,520"/>
    <circle cx="204" cy="560" r="9"/>
    <circle cx="356" cy="560" r="9"/>
    <rect x="0" y="605" width="373" height="515"/>
    <rect x="380" y="605" width="373" height="515"/>
    <path d="M753,690 L836,740 M753,1120 L836,1090"/>
    <circle cx="805" cy="920" r="8"/>
    <circle cx="805" cy="995" r="8"/>
    <path d="M384,1120 L400,1180 L735,1180 L752,1120"/>
    <circle cx="500" cy="1150" r="8"/>
    <circle cx="640" cy="1150" r="8"/>
  </svg>

</main>
</body>
</html>
```